Dental Hygiene referral cards

I am looking to make some referral cards for our hygienists for our dental office. something with our logo and address on the front, and on the back have
hygienist:
__________________
Referred by:
__________________
with a little blurb about what we will give away for a referral.

attached to this is our logo, and a drawing of what im looking for.

I will need this for two of our offices, so just the logo and address will change.

```html
<!DOCTYPE html>
<html lang="en">
<head>
<meta charset="utf-8">
<title>Harbour Ridge Dental – Referral Card</title>
<link rel="stylesheet" href="https://fonts.googleapis.com/css2?family=Roboto:wght@400;500&display=swap">
<style>
  :root {
    --brand-blue: #01427e;
    --text-grey: #777777;
    --blurb-grey: #9a9a9a;
    --ink: #1a1a1a;
    --paper: #ffffff;
  }
  * { box-sizing: border-box; margin: 0; padding: 0; }
  html, body { width: 1200px; height: 1200px; overflow: hidden; background: var(--paper); }
  body { position: relative; font-family: "Roboto", Arial, sans-serif; }

  .card-front, .card-back { position: absolute; left: 0; top: 0; width: 1200px; height: 1200px; }

  .brand-mark {
    position: absolute; display: flex; align-items: center; gap: 14px;
    color: var(--brand-blue); font-weight: 500; line-height: 1.05;
  }
  .brand-mark__dot { flex: none; border-radius: 50%; background: var(--brand-blue); }
  .brand-mark--front { left: 272px; top: 252px; width: 340px; font-size: 36px; }
  .brand-mark--front .brand-mark__dot { width: 44px; height: 44px; }
  .brand-mark--back { left: 730px; top: 650px; width: 260px; font-size: 30px; }
  .brand-mark--back .brand-mark__dot { width: 36px; height: 36px; }

  .divider { position: absolute; left: 629px; top: 216px; width: 1.5px; height: 165px; background: var(--brand-blue); }

  .contact { position: absolute; left: 678px; top: 200px; }
  .contact__name { font-size: 37px; font-weight: 500; color: var(--brand-blue); line-height: 1.1; }
  .contact__role { font-size: 22px; color: var(--text-grey); margin-top: 2px; }
  .contact__list { list-style: none; margin-top: 14px; }
  .contact__item { display: flex; align-items: center; gap: 9px; font-size: 22.5px; color: var(--ink); height: 26.5px; }
  .contact__icon { width: 18px; height: 18px; flex: none; fill: var(--brand-blue); }

  .band { position: absolute; left: 209px; top: 509px; width: 840px; height: 30px; background: var(--brand-blue); }

  .offer-triangle { position: absolute; left: 212px; top: 616px; }
  .offer-headline {
    position: absolute; left: 218px; top: 626px;
    color: var(--paper); font-size: 30px; font-weight: 500; line-height: 36px;
  }

  .referral-field { position: absolute; left: 347px; color: var(--brand-blue); font-size: 35px; font-weight: 400; }
  .referral-field--hygienist { top: 818px; }
  .referral-field--referrer { top: 886px; }

  .blurb {
    position: absolute; left: 242px; top: 989px; width: 800px;
    text-align: center; color: var(--blurb-grey); font-size: 19.5px; line-height: 24px; font-weight: 400;
  }
</style>
</head>
<body>
  <section class="card-front">
    <div class="brand-mark brand-mark--front">
      <span class="brand-mark__dot"></span>
      <span class="brand-mark__name">HARBOUR RIDGE<br>DENTAL</span>
    </div>
    <div class="divider"></div>
    <div class="contact">
      <h1 class="contact__name">ALEX MORGAN</h1>
      <p class="contact__role">DIRECTOR</p>
      <ul class="contact__list">
        <li class="contact__item">
          <svg class="contact__icon" viewBox="0 0 24 24"><path d="M6.6 10.8a15.1 15.1 0 0 0 6.6 6.6l2.2-2.2a1 1 0 0 1 1-.25 11.4 11.4 0 0 0 3.6.57 1 1 0 0 1 1 1V20a1 1 0 0 1-1 1A17 17 0 0 1 3 4a1 1 0 0 1 1-1h3.5a1 1 0 0 1 1 1c0 1.25.2 2.45.57 3.57a1 1 0 0 1-.25 1z"/></svg>
          +0400 555 010
        </li>
        <li class="contact__item">
          <svg class="contact__icon" viewBox="0 0 24 24"><path d="M6.6 10.8a15.1 15.1 0 0 0 6.6 6.6l2.2-2.2a1 1 0 0 1 1-.25 11.4 11.4 0 0 0 3.6.57 1 1 0 0 1 1 1V20a1 1 0 0 1-1 1A17 17 0 0 1 3 4a1 1 0 0 1 1-1h3.5a1 1 0 0 1 1 1c0 1.25.2 2.45.57 3.57a1 1 0 0 1-.25 1z"/></svg>
          +02 5550 0199
        </li>
        <li class="contact__item">
          <svg class="contact__icon" viewBox="0 0 24 24"><path d="M3 6h18v12H3z M3 6l9 7 9-7" stroke="#fff" stroke-width="1.5"/></svg>
          alexmorgan@mail.com
        </li>
        <li class="contact__item">
          <svg class="contact__icon" viewBox="0 0 24 24"><circle cx="12" cy="12" r="9"/><path d="M3 12h18M12 3c3 3 3 15 0 18M12 3c-3 3-3 15 0 18" stroke="#fff" stroke-width="1.2" fill="none"/></svg>
          www.harbourridgedental.com
        </li>
      </ul>
    </div>
  </section>

  <div class="band"></div>

  <section class="card-back">
    <svg class="offer-triangle" width="340" height="327" viewBox="0 0 340 327" aria-hidden="true">
      <polygon points="0,0 340,0 0,327" fill="var(--brand-blue)"/>
    </svg>
    <p class="offer-headline">FREE<br>PULSECLEAN<br>TOOTHBRUSH!</p>

    <p class="referral-field referral-field--hygienist">HYGENIST:</p>
    <p class="referral-field referral-field--referrer">REFERRED BY:</p>

    <div class="brand-mark brand-mark--back">
      <span class="brand-mark__dot"></span>
      <span class="brand-mark__name">HARBOUR RIDGE<br>DENTAL</span>
    </div>

    <p class="blurb">REFER A PATIENT FOR AN EXAM AND A CLEANING AND BOTH<br>OF YOU WILL RECIVE A FREE PULSECLEAN TOOTHBRUSH.</p>
  </section>
</body>
</html>
```